New Business Card Design Project

I need a design for business cards, i am an electrical business called "Vantor Electrical and Communications" i need the cards to be double sided with the company logo on the back (attached) the front needs to say my company name, web site, email address, telephone number, and ABN number and electrical license number. I am open to different arrangements of the information but would like the background to be incorporating something electrical or something that looks smart. open to all additional ideas also.

The company colours are orange and grey see logo attached.

Business Name: Vantor Electrical and Communications
Website: vantorelectricalandcomms.example.au
Email: dean@vantorelectricalandcomms.example.au
Telephone(mobile): 0481290736
ABN: 71829304516
Lic No: 483027D

Target Market(s)

Business entities, Project Managers, Accounts, Clients

Industry/Entity Type

Electrician

Contact Information for Business Card

I need a design for business cards, i am an electrical business called "Vantor Electrical and Communications" i need the cards to be double sided with the company logo on the back (attached) the front needs to say my company name

Font styles to use
Serif
Sans Serif

Colors
f37122
5c5c5c

Requirements
Must have
• Must have the Logo on the back open to different ways of it being on the back but had in mind to keep it central but again open to other options
Nice to have
• A real modern cool background that is eye catching yet contemporary
Should not have
• No backgrounds of a light bulb or plug or anything like that

```html
<!DOCTYPE html>
<html lang="en">
<head>
<meta charset="utf-8">
<title>Vantor Electrical and Communications – Business Cards</title>
<link rel="stylesheet" href="https://fonts.googleapis.com/css2?family=Questrial&display=swap">
<style>
  :root {
    --orange: #f5a01a;
    --brand-orange: #f37122;
    --grey: #5c5c5c;
    --card-dark: #58585a;
    --text-dark: #4a4a4a;
    --white: #ffffff;
    --backdrop: #2e2e2e;
  }
  * { box-sizing: border-box; margin: 0; padding: 0; }
  html, body { width: 1200px; height: 900px; overflow: hidden; }
  body {
    background: var(--backdrop);
    font-family: "Questrial", sans-serif;
    position: relative;
  }
  .card {
    position: absolute;
    width: 560px;
    height: 320px;
    border-radius: 22px;
    overflow: hidden;
  }
  .card-back { left: 80px; top: 100px; background: var(--card-dark); }
  .card-front { left: 560px; top: 480px; background: var(--white); }

  .back-logo {
    position: absolute;
    left: 0; right: 0; top: 100px;
    text-align: center;
    color: var(--orange);
  }
  .back-logo .brand-name {
    font-size: 58px;
    letter-spacing: 6px;
    line-height: 1;
  }
  .back-logo .brand-sub {
    font-size: 17px;
    letter-spacing: 2.5px;
    margin-top: 10px;
    text-transform: uppercase;
  }
  .back-web {
    position: absolute;
    left: 30px; bottom: 26px;
    font-size: 17px;
    color: var(--white);
  }
  .back-web .domain { color: var(--orange); }

  .front-logo {
    position: absolute;
    right: 34px; top: 36px;
    text-align: left;
    color: var(--orange);
    width: 260px;
  }
  .front-logo .brand-name {
    font-size: 40px;
    letter-spacing: 4px;
    line-height: 1;
  }
  .front-logo .brand-sub {
    font-size: 11.5px;
    letter-spacing: 1.6px;
    text-transform: uppercase;
    margin-top: 6px;
  }
  .licence {
    position: absolute;
    left: 266px; top: 116px;
    font-size: 13px;
    color: var(--text-dark);
  }
  .label { color: var(--orange); }

  .side-tab {
    position: absolute;
    left: 0; top: 200px; bottom: 0;
    width: 26px;
    background: var(--grey);
    border-top-right-radius: 18px;
  }
  .contact {
    position: absolute;
    left: 46px; bottom: 26px;
    color: var(--text-dark);
  }
  .person-name {
    font-size: 28px;
    color: var(--orange);
    text-transform: uppercase;
    letter-spacing: 0.5px;
    line-height: 1;
  }
  .person-role { font-size: 14px; margin-top: 4px; letter-spacing: 0.5px; }
  .abn { font-size: 14px; margin-top: 3px; margin-bottom: 10px; }
  .contact-line {
    display: flex; align-items: center; gap: 8px;
    font-size: 14px; line-height: 20px;
  }
  .contact-line svg { width: 12px; height: 12px; flex: none; }
</style>
</head>
<body>

<section class="card card-back" aria-label="Business card back">
  <div class="back-logo">
    <div class="brand-name">VANTOR</div>
    <div class="brand-sub">Electrical &amp; Communications</div>
  </div>
  <div class="back-web">www.<span class="domain">vantorelectricalandcomms</span>.example.au</div>
</section>

<section class="card card-front" aria-label="Business card front">
  <div class="front-logo">
    <div class="brand-name">VANTOR</div>
    <div class="brand-sub">Electrical &amp; Communications</div>
  </div>
  <div class="licence"><span class="label">Lic No:</span> 483027D</div>

  <div class="side-tab"></div>

  <div class="contact">
    <div class="person-name">Marlo Quintrell</div>
    <div class="person-role">DIRECTOR</div>
    <div class="abn"><span class="label">ABN:</span> 71829304516</div>
    <div class="contact-line">
      <svg viewBox="0 0 12 12"><path d="M2.5 1 L4.5 1 L5 3.5 L3.8 4.4 Q5 7 7.6 8.2 L8.5 7 L11 7.5 L11 9.5 Q10.5 11 9 11 Q1 10 1 2.5 Q1 1 2.5 1 Z" fill="var(--orange)"/></svg>
      <span>0481 290 736</span>
    </div>
    <div class="contact-line">
      <svg viewBox="0 0 12 12"><rect x="1" y="2.5" width="10" height="7" fill="none" stroke="var(--orange)" stroke-width="1.2"/><path d="M1 2.5 L6 6.5 L11 2.5" fill="none" stroke="var(--orange)" stroke-width="1.2"/></svg>
      <span>dean@vantorelectricalandcomms.example.au</span>
    </div>
    <div class="contact-line">
      <svg viewBox="0 0 12 12"><circle cx="6" cy="6" r="4.8" fill="none" stroke="var(--orange)" stroke-width="1.1"/><ellipse cx="6" cy="6" rx="2" ry="4.8" fill="none" stroke="var(--orange)" stroke-width="1"/><path d="M1.2 6 H10.8" stroke="var(--orange)" stroke-width="1"/></svg>
      <span>www.vantorelectricalandcomms.example.au</span>
    </div>
  </div>
</section>

</body>
</html>
```